Redesign Website for Tandara Flame

I have an existing website on https://www.tandaraflame-example.com.au/ and would like to have this redesigned professionally with new content (please refer to word document). We are fire protection engineers providing fire services design expertise and engineering design to a range of different clients.

We also provide drafting services to clients in the form of completing final commissioning documentation such as 'as-installed' drawings and fire services block plans to ensure compliance with the building code and relevant Australian Standards.

Target Market(s)

Builders, Architects, Consultants, Project Managers

Industry/Entity Type

Engineering Consultant

Coding

Coded - Design and coding required

Number of Pages Required

4 page

Font styles to use
Sans Serif

Requirements
Must have
• Home and about Page, fire services design page, fire block plans page, contact us page (4 Pages).

The website colour choice must match or compliment the new company logo.
Nice to have
• Quality photos of fire services installations in buildings to Australian Standards.

A website similar to this would be ideal http://corbellpyro-example.com.au
Should not have
• Stolen licensed photos

```html
<!DOCTYPE html>
<html lang="en">
<head>
<meta charset="utf-8">
<title>Fire Block Plans – Tandara Flame</title>
<link href="https://fonts.googleapis.com/css2?family=Outfit:wght@300;400;500;600;700&family=Tinos:wght@700&display=swap" rel="stylesheet">
<style>
  :root {
    --orange: #f7941d;
    --ink: #1a1a1a;
    --text: #2a2a2a;
    --white: #ffffff;
    --footer-bg: #2c3035;
    --footer-line: #4a4e53;
    --footer-text: #d9d9d9;
    --card-border: #e2e2e2;
  }
  * { margin: 0; padding: 0; box-sizing: border-box; }
  html, body { width: 996px; height: 1200px; overflow: hidden; background: var(--white); }
  body { position: relative; font-family: "Outfit", sans-serif; color: var(--text); }
  .abs { position: absolute; }

  /* Header */
  .site-header { position: absolute; left: 0; top: 0; width: 996px; height: 67px; background: var(--white); z-index: 2; }
  .nav-link { position: absolute; top: 27px; font-size: 12px; color: var(--text); text-decoration: none; line-height: 16px; }
  .brand-tab { position: absolute; left: 416px; top: 0; width: 164px; height: 85px; z-index: 3; }
  .brand-tab svg { position: absolute; left: 0; top: 0; }
  .brand-mark { position: absolute; left: 74px; top: 26px; width: 16px; height: 16px; border-radius: 50%; background: var(--orange); }
  .brand-name { position: absolute; left: 0; top: 62px; width: 164px; text-align: center; font-weight: 600; font-size: 13px; color: var(--orange); letter-spacing: 0.2px; }

  /* Hero */
  .hero { position: absolute; left: 0; top: 67px; width: 996px; height: 311px;
    background: linear-gradient(180deg, #3b3d3f 0%, #6b6e70 45%, #8d8f90 70%, #4e5153 100%); }
  .hero-title { position: absolute; left: 0; top: 208px; width: 996px; text-align: center;
    font-family: "Tinos", serif; font-weight: 700; font-size: 30px; color: var(--white); line-height: 36px; }

  /* Intro */
  .divider { position: absolute; left: 441px; top: 440px; width: 114px; height: 22px; }
  .intro { position: absolute; left: 160px; top: 480px; width: 676px; text-align: center;
    font-size: 17px; line-height: 30px; color: var(--text); }

  /* Pricing */
  .plan { position: absolute; top: 659px; width: 218px; height: 252px; border: 1px solid var(--card-border);
    background: var(--white); box-shadow: 0 6px 14px rgba(0,0,0,0.06); text-align: center; }
  .plan--featured { background: var(--orange); border-color: var(--orange); box-shadow: none; color: var(--white); }
  .plan-name { position: absolute; left: 0; top: 40px; width: 100%; font-size: 13px; line-height: 16px; }
  .plan-price { position: absolute; left: 0; top: 79px; width: 100%; font-size: 56px; font-weight: 700; line-height: 72px; color: var(--ink); letter-spacing: -1px; }
  .plan--featured .plan-price { color: var(--white); }
  .plan-rule { position: absolute; left: 98px; top: 155px; width: 22px; height: 3px; background: var(--orange); }
  .plan--featured .plan-rule { background: var(--white); }
  .quote-btn { position: absolute; left: 40px; top: 174px; width: 137px; height: 34px; }
  .quote-btn span { position: absolute; left: 0; top: 0; width: 100%; line-height: 34px; font-size: 10px; font-weight: 600; color: var(--white); }
  .quote-btn--solid { background: var(--orange); clip-path: polygon(8% 0, 92% 0, 100% 50%, 92% 100%, 8% 100%, 0 50%); }

  /* Footer */
  .site-footer { position: absolute; left: 0; top: 973px; width: 996px; height: 227px;
    background: linear-gradient(160deg, #30343a 0%, #2a2e33 50%, #34383d 100%); color: var(--footer-text); }
  .footer-brand { position: absolute; left: 170px; top: 37px; width: 115px; text-align: center; }
  .footer-brand-mark { width: 24px; height: 24px; border-radius: 50%; background: var(--orange); margin: 0 auto 8px; }
  .footer-brand-name { font-size: 14px; font-weight: 600; color: var(--orange); }
  .social { position: absolute; top: 113px; width: 22px; height: 22px; border: 1.5px solid var(--white); border-radius: 50%; }
  .footer-heading { position: absolute; top: 48px; font-family: "Tinos", serif; font-weight: 700; font-size: 11px; color: var(--white); }
  .footer-heading::after { content: ""; position: absolute; left: 0; top: 19px; width: 31px; height: 2px; background: var(--orange); }
  .footer-list { position: absolute; top: 84px; list-style: none; font-size: 8.5px; font-weight: 300; line-height: 18.7px; color: var(--footer-text); }
  .newsletter { position: absolute; left: 663px; top: 96px; width: 172px; height: 27px; }
  .newsletter-field { position: absolute; left: 0; top: 0; width: 172px; height: 27px; background: var(--white);
    clip-path: polygon(4% 0, 96% 0, 100% 50%, 96% 100%, 4% 100%, 0 50%); }
  .newsletter-field span { position: absolute; left: 16px; top: 0; line-height: 27px; font-size: 8px; color: #888; }
  .newsletter-btn { position: absolute; left: 105px; top: 3px; width: 62px; height: 21px; background: var(--orange);
    clip-path: polygon(8% 0, 92% 0, 100% 50%, 92% 100%, 8% 100%, 0 50%);
    font-family: "Tinos", serif; font-weight: 700; font-size: 8px; color: var(--white); text-align: center; line-height: 21px; }
  .footer-rule { position: absolute; left: 153px; top: 191px; width: 690px; height: 1px; background: var(--footer-line); }
  .footer-copy { position: absolute; left: 153px; top: 203px; font-size: 8px; font-weight: 300; color: #aaa; }
  .footer-legal { position: absolute; right: 153px; top: 203px; font-size: 8px; font-weight: 300; color: #aaa; }
</style>
</head>
<body>

<header class="site-header">
  <a class="nav-link" style="left:225px" href="#">Home</a>
  <a class="nav-link" style="left:308px" href="#">Fire Services</a>
  <a class="nav-link" style="left:611px" href="#">Fire Block Plans</a>
  <a class="nav-link" style="left:746px" href="#">Contact Us</a>
</header>

<div class="brand-tab">
  <svg width="164" height="85" viewBox="0 0 164 85"><polygon points="0,67 164,67 146,85 18,85" fill="#ffffff"/></svg>
  <div class="brand-mark"></div>
  <div class="brand-name">TANDARA FLAME</div>
</div>

<section class="hero" role="img" aria-label="Photo of an empty underground car park with concrete columns and fire service pipework">
</section>
<h1 class="hero-title">Fire Block Plans</h1>

<svg class="divider" viewBox="0 0 114 22" width="114" height="22">
  <line x1="0" y1="11" x2="114" y2="11" stroke="#f7941d" stroke-width="2"/>
  <circle cx="57" cy="11" r="9" fill="#ffffff" stroke="#f7941d" stroke-width="2"/>
</svg>

<p class="intro">We can also assist our clients in the preparation commissioning documentation (i.e. zone block plan, fire hydrant block plans, sprinkler block plan) as required for relevant fire safety systems on completion of a project to achieve full compliance with relevant Australian Standards for project handover or for the update of existing outdated / missing block plans.</p>

<div class="plan" style="left:153px">
  <div class="plan-name">Zone<br>Block Plan</div>
  <div class="plan-price">$80</div>
  <div class="plan-rule"></div>
  <div class="quote-btn quote-btn--solid"><span>GET A QUOTE</span></div>
</div>

<div class="plan plan--featured" style="left:389px">
  <div class="plan-name">Fire<br>Hydrant Block Plans</div>
  <div class="plan-price">$100</div>
  <div class="plan-rule"></div>
  <div class="quote-btn">
    <svg width="137" height="34" viewBox="0 0 137 34" class="abs" style="left:0;top:0">
      <polygon points="11,1 126,1 136,17 126,33 11,33 1,17" fill="none" stroke="#ffffff" stroke-width="1.5"/>
    </svg>
    <span>GET A QUOTE</span>
  </div>
</div>

<div class="plan" style="left:626px">
  <div class="plan-name">Sprinkler<br>Block Plan</div>
  <div class="plan-price">$120</div>
  <div class="plan-rule"></div>
  <div class="quote-btn quote-btn--solid"><span>GET A QUOTE</span></div>
</div>

<footer class="site-footer" role="img" aria-label="Dimmed photo of a car park behind the footer content">
  <div class="footer-brand">
    <div class="footer-brand-mark"></div>
    <div class="footer-brand-name">TANDARA FLAME</div>
  </div>
  <span class="social" style="left:175px"></span>
  <span class="social" style="left:203px"></span>
  <span class="social" style="left:230px"></span>
  <span class="social" style="left:257px"></span>

  <div class="footer-heading" style="left:322px">Quick Links</div>
  <ul class="footer-list" style="left:322px">
    <li>Home</li><li>About Us</li><li>Fire Services</li><li>Fire Block Plans</li><li>Contact Us</li>
  </ul>

  <div class="footer-heading" style="left:428px">Fire Services</div>
  <ul class="footer-list" style="left:428px">
    <li>Smoke Alarms</li><li>Fire Hydrants</li><li>Emergency Lighting</li><li>Exit Signs</li><li>See All »</li>
  </ul>

  <div class="footer-heading" style="left:523px">Fire Block Plans</div>
  <ul class="footer-list" style="left:523px">
    <li>Zone Block Plan</li><li>Fire Hydrant Block Plans</li><li>Sprinkler Block Plans</li>
  </ul>

  <div class="footer-heading" style="left:662px">Subscribe Our Newsletter</div>
  <div class="newsletter">
    <div class="newsletter-field"><span>Email...</span></div>
    <div class="newsletter-btn">Subscribe!</div>
  </div>

  <div class="footer-rule"></div>
  <div class="footer-copy">© Copyright Tandara Flame 2021, All Rights Reserved.</div>
  <div class="footer-legal">Privacy Policy &nbsp;|&nbsp; Terms &amp; Conditions</div>
</footer>

</body>
</html>
```